Gestaltung eines Merkblattes
Ein Entwurf, der genau meinen Vorstellungen entspricht. Eine Abwicklung, die schneller und professioneller nicht sein könnte. Die Kommunikation - sehr symphatisch und kundenorientiert. Resumee: Besser geht es nicht.
Zielgruppe
www.tierklang-analytik.de/ Medizinische Bioresonanzanalysen für Pferde. Die Kundschaft besteht hauptsächlich aus Frauen, Alter von 20- 55 Jahre.
Bei dem Projekt handelt es sich um die Gestaltung eines wichtigen Merkblattes, das jedem Kunde zusammen mit dem Befund der Analyse gemailt wird. Es enthält wichtige Informationen rund um die Bioresonanzanalyse und sollte als pdf- Datei vorliegen.
Aufgabenstellung
Kernproblem: Die Kunden lesen das Merkblatt gar nicht oder nicht sorgfältig. So entstehen viele Fragen in der Folge, die nicht notwendig wären.
Wir benötigen eine pdf- Datei, die zum Lesen anregt, gerne gelesen wird und in der die wichtigsten Aspekte in das Auge fallen. Diese wurden von mir in der Worddatei, die den Text enthält, rot markiert.
Der Text in schwarz ist deutlich weniger wichtig.
Ach ja, die Überschrift ist doof. 'Allgemeine Hinweise' das animiert nicht wirklich zum Lesen. Falls Sie eine griffige Idee haben, sehr gerne.

```html
<!DOCTYPE html>
<html lang="de">
<head>
<meta charset="utf-8">
<title>Merkblatt – Wichtige Hinweise</title>
<link rel="stylesheet" href="https://fonts.googleapis.com/css2?family=Fira+Sans:wght@400;500;600;700&display=swap">
<style>
  :root {
    --canvas: #e7e4df;
    --paper: #ffffff;
    --green: #a9b86c;
    --pale: #eff1e2;
    --pale-strong: #e2e6cc;
    --strip: #dcdcdc;
    --ink: #333333;
    --ink-dark: #222222;
    --muted: #6f6f6f;
  }
  * { box-sizing: border-box; margin: 0; padding: 0; }
  html, body { width: 1200px; height: 800px; overflow: hidden; }
  body {
    background: var(--canvas);
    font-family: "Fira Sans", Arial, sans-serif;
    color: var(--ink);
    position: relative;
  }
  .page {
    position: absolute;
    top: 20px;
    width: 535px;
    height: 760px;
    background: var(--paper);
    overflow: hidden;
  }
  .page--front { left: 60px; }
  .page--back { left: 605px; }

  /* Front page header */
  .brand {
    position: absolute;
    top: 52px; left: 0; right: 0;
    text-align: center;
  }
  .brand__name {
    display: inline-flex;
    align-items: center;
    gap: 8px;
    font-size: 24px;
    font-weight: 600;
    color: var(--green);
    letter-spacing: 1px;
  }
  .brand__dot {
    width: 12px; height: 12px; border-radius: 50%;
    background: var(--green);
  }
  .brand__tagline {
    margin-top: 6px;
    font-size: 5.5px;
    letter-spacing: 1px;
    color: var(--green);
  }
  .contact {
    position: absolute;
    top: 144px; left: 0; right: 0;
    text-align: center;
    font-size: 8.4px;
    line-height: 11px;
    color: var(--muted);
  }
  .title-band {
    position: absolute;
    top: 183px; left: 0; right: 0;
    height: 47px;
    background: var(--green);
    color: #fff;
    font-size: 21px;
    font-weight: 600;
    display: flex; align-items: center; justify-content: center;
    letter-spacing: .3px;
  }

  /* Info boxes */
  .card {
    position: absolute;
    width: 246px;
    background: var(--pale);
    padding: 9px 12px 0 12px;
  }
  .card--l { left: 14px; }
  .card--r { left: 275px; }
  .heading {
    font-size: 12.6px;
    font-weight: 500;
    color: var(--ink-dark);
    line-height: 16px;
    margin-bottom: 8px;
  }
  .text {
    font-size: 8.6px;
    line-height: 11.8px;
    text-align: justify;
    hyphens: auto;
  }
  .text + .text { margin-top: 11.8px; }
  .text--tight + .text--tight { margin-top: 0; }
  .text strong { font-weight: 600; }

  /* Back page */
  .top-strip {
    position: absolute; top: 0; left: 0; right: 0; height: 13px;
    background: var(--strip);
  }
  .section {
    position: absolute;
    padding: 0 13px 0 25px;
  }
  .col-a { left: 0; width: 260px; }
  .col-b { left: 276px; width: 260px; padding: 0 25px 0 13px; }
  .section--pale { background: var(--pale); }
  .section--strong { background: var(--pale-strong); }
  .tab {
    position: absolute;
    width: 8px; height: 31px;
    background: var(--green);
  }
  .col-a .tab { left: 0; }
  .col-b .tab { right: 0; }
  .photo { position: absolute; }
  .photo--vet {
    left: 0; top: 312px; width: 260px; height: 121px;
    background: linear-gradient(100deg, #2e3042 0%, #3b3848 30%, #7a4a2e 55%, #9a5f3a 80%, #6f4128 100%);
  }
  .photo--coast {
    left: 276px; top: 530px; width: 260px; height: 230px;
    background: linear-gradient(180deg, #8d959b 0%, #a8b0b4 30%, #7b8287 55%, #5e5b56 78%, #3f3b37 100%);
  }
</style>
</head>
<body>

<section class="page page--front">
  <div class="brand">
    <div class="brand__name"><span class="brand__dot"></span>TIERKLANG ANALYTIK</div>
    <div class="brand__tagline">MEDIZINISCHE ANALYSEN FÜR PFERDE</div>
  </div>
  <div class="contact">
    Inh. Carola Wendtland · Lindenweg 4 · 36100 Musterbach<br>
    Mail: info@tierklang-analytik.de · Tel. +49 (0) 1234 567890
  </div>
  <h1 class="title-band">Wichtige Hinweise - bitte unbedingt lesen!</h1>

  <article class="card card--l" style="top:246px;height:173px;">
    <h2 class="heading">Wie verabreiche ich die Präparate?</h2>
    <p class="text">Die empfohlenen Präparate können (wenn nicht anders angegeben) in das normale Kraftfutter gegeben werden. Tropfen und Bachblüten bitte auf ein kleines Stück trockenes Brot, Zwieback, bei Pferden, die kein Getreide fressen dürfen, auf ein Stück Reiswaffel geben, und dem Pferd direkt füttern.</p>
    <p class="text">Vitalbase Pulver muss nicht, wie vom Hersteller angegeben, in Wasser aufgelöst werden. Eine Gabe in das Kraftfutter, Heucobs etc. vermindert nicht die Wirkung.</p>
  </article>

  <article class="card card--l" style="top:444px;height:119px;">
    <h2 class="heading">Wie lange gebe ich die Präparate?</h2>
    <p class="text">Bitte füttern Sie alle Präparate, außer es sind abweichende Empfehlungen vorhanden, ohne Unterbrechung, bis Ihnen das Ergebnis der ersten Nachtestung vorliegt. Pausen von mehr als zwei Tagen können zu Beginn der Behandlung die positive Entwicklung Ihres Pferdes beeinträchtigen.</p>
  </article>

  <article class="card card--l" style="top:588px;height:144px;">
    <h2 class="heading">Hilfe, mein Pferd frisst das nicht...</h2>
    <p class="text">Falls Ihr Pferd sehr wählerisch ist bei der Zufütterung von Präparaten in Pellets- oder Pulverform, dann beginnen Sie mit einer sehr kleinen Dosierung von z. b. ½ Teelöffel und steigern diese sehr langsam. Bei trockenem Futter (Müsli, Hafer) sortieren manche Pferde gerne aus. Hier ist es sinnvoll, das Futter an zu feuchten, etwas Heucobs oder getreidefreies Mash dazuzugeben.</p>
  </article>

  <article class="card card--r" style="top:246px;height:140px;">
    <h2 class="heading">Wie läuft das mit einer Nachtestung?</h2>
    <p class="text text--tight">Wir bestätigen den Eingang der Probe zur Nachtestung nicht. In regelmäßigen Abständen werden alle Befunde nachgetestet. Wir senden Ihnen im Anschluss per Mail das neue Ergebnis mit einer aktualisierten Therapieempfehlung zu.</p>
    <p class="text text--tight">Wir brauchen für die Nachtestung eine neue Haarprobe und ein kurzes Feedback zu der aktuellen Entwicklung Ihres Pferdes. Mehr nicht.</p>
  </article>

  <article class="card card--r" style="top:402px;height:162px;">
    <h2 class="heading">Wozu eine Bachblüten-Therapie?</h2>
    <p class="text">Wenn die Therapieempfehlung eine Übersicht an Bachblüten enthält, dann spiegeln diese den seelischen Zustand Ihres Pferdes wieder, der von seinen aktuellen Lebensbedingungen, seiner körperlichen Belastung durch Krankheit und durch Abläufe in seiner Herde beeinflusst wird. Erfahrungsgemäß bezieht sich die Darstellung der Blüten bei Pferden, die in einer Herde leben, häufig mehr auf die Gefühle des Pferdes gegenüber seinen Artgenossen als auf den Kontakt mit dem Menschen.</p>
  </article>

  <article class="card card--r" style="top:580px;height:152px;">
    <h2 class="heading">Wo gibt es die Bachblütenmischung?</h2>
    <p class="text">Die meisten Apotheken kennen sich aus mit der Herstellung einer Bachblütenmischung. Falls nicht, hier die Anleitung: in ein 30 ml Medizinfläschchen mit Tropfvorrichtung oder Pipette gibt man 10 ml Alkohol (Brandy oder Weinbrand), 20 ml Quellwasser oder stilles Mineralwasser (ohne Kohlensäure; kein destilliertes Wasser!) und 2-3 Tropfen von jeder Blüte, die im Moment benötigt wird. Als Alternative zu Alkohol kann auch Obstessig eingesetzt werden.</p>
  </article>
</section>

<section class="page page--back">
  <div class="top-strip"></div>

  <!-- Column A -->
  <div class="tab" style="top:27px;left:0;"></div>
  <div class="section col-a" style="top:25px;">
    <h2 class="heading" style="margin:0;">Der Tierarzt kommt zu einem anderen Ergebnis...</h2>
  </div>
  <div class="section section--pale col-a" style="top:73px;height:68px;padding-top:10px;">
    <p class="text"><strong>Wir weisen ausdrücklich darauf hin, dass die Ergebnisse der Bioresonanzanalyse nicht kompatibel sind mit den herkömmlichen Labormethoden und anderen tierärztlichen Diagnoseformen.</strong></p>
  </div>
  <div class="section col-a" style="top:155px;">
    <p class="text">Ein Beispiel: Wenn wir eine Belastung der Leber mit dem Leberegel Fasciola hepatica feststellen, kann eine klassische Laboruntersuchung zu dem gleichen Thema ergebnislos bleiben. Der Grund hierfür liegt u.a. in der sehr unterschiedlichen Beurteilung und Herangehensweise.</p>
    <p class="text">Das Wohl Ihres Pferdes steht jederzeit im Mittelpunkt. Falls in der Zeit der Umsetzung der Therapieempfehlung bei Ihrem Pferd Symptome auftreten, die eine tierärztliche und schnelle Hilfe dringend erforderlich machen, zögern Sie bitte nie, den Tierarzt zu rufen.</p>
  </div>

  <div class="photo photo--vet" role="img" aria-label="Foto: behandschuhte Hand hält ein Stethoskop an das braune Fell eines Pferdes"></div>

  <div class="section section--pale col-a" style="top:433px;height:170px;padding-top:14px;">
    <h2 class="heading">Das Pferd bekommt schon andere Medikamente...</h2>
    <p class="text">Bitte informieren Sie mich vorab, wenn Ihr Pferd zum Zeitpunkt der Nachtestung Medikamente von dem Tierarzt erhält. Relevant sind Antibiotika, Cortison, sowie andere, massiv entzündungshemmende Präparate. In diesem Fall sprechen wir miteinander ab, ob die Nachtestung verschoben wird. Wurmkuren und Impfungen sind für die Durchführung der Nachtestung nicht von Bedeutung.</p>
  </div>
  <div class="tab" style="top:447px;left:0;"></div>

  <div class="section col-a" style="top:613px;">
    <h2 class="heading">Wann macht eine Impfung Sinn?</h2>
    <p class="text">Wir geben generell keine Impfempfehlungen. Es hat sich jedoch in den vergangenen Jahren gezeigt, dass es sinnvoll ist, Impfungen (besonders Influenza- und Herpes- Impfungen) vor Beginn der Umsetzung der Therapieempfehlung einzuplanen. Werden sie zu einem späteren Zeitpunkt vorgenommen, kann es zu Rückschritten in der ansonsten positiven Entwicklung kommen.</p>
  </div>
  <div class="tab" style="top:614px;left:0;height:30px;"></div>

  <!-- Column B -->
  <div class="section section--pale col-b" style="top:13px;height:339px;padding-top:12px;">
    <h2 class="heading">Karenzzeit bei evtl. Doping-Kontrollen</h2>
    <p class="text">Zum Schutz der Pferde bestehen Anti-Doping Richtlinien, die klare Regeln vorgeben, welche Zusatzfutterpräparate, Medikamente und auch Naturheilmittel einem Turnierpferd vor und während einem Start in einer Turnierprüfung gefüttert werden dürfen. Die Einhaltung der Vorgaben wird durch stichpunktartige Kontrollen überprüft.</p>
    <p class="text">Bitte beachten Sie die Anti-Doping Richtlinien der Reitsportdachverbände und weiterer Pferdesportverbände und halten Sie bei der Fütterung aller Präparate unserer Therapieempfehlung eine Karenzzeit von 48 Stunden vor Prüfungsbeginn ein, wenn Sie mit Ihrem Pferd an einem Wettbewerb teilnehmen.</p>
  </div>
  <div class="section section--strong col-b" style="top:232px;height:60px;padding-top:12px;">
    <p class="text"><strong>Ausnahme:<br>Bei der Zufütterung von Präparaten, die Teufelskralle enthalten, besteht eine Karenzzeit von 4 Tagen.</strong></p>
  </div>
  <div class="section col-b" style="top:304px;">
    <p class="text">Wir übernehmen für die Folgen einer Nichtbeachtung der nationalen oder internationalen Anti-Dopingrichtlinien keine Haftung.</p>
  </div>
  <div class="tab" style="top:27px;right:0;left:auto;"></div>

  <div class="section col-b" style="top:363px;">
    <h2 class="heading">Dürfen tragende Stuten / Stuten mit Fohlen bei Fuß therapiert werden?</h2>
    <p class="text">Wir übernehmen keine Haftung für die Gabe der von uns empfohlenen Naturheilmittel bei tragenden Stute und Stuten mit Fohlen bei Fuß. Jedes der angegebenen Mittel wurde von mir mit großer Sorgfalt ausgewählt. Die aktuell vorhandenen, medizinischen Studien zu der Wirkung von Naturheilmitteln bei tragenden Stuten sind jedoch nicht umfangreich genug, um Nebenwirkungen vollständig ausschließen zu können.</p>
  </div>
  <div class="tab" style="top:363px;right:0;left:auto;"></div>

  <div class="photo photo--coast" role="img" aria-label="Foto: Islandpferd steht auf Felsen an einer nebligen Küste vor Bergen"></div>
</section>

</body>
</html>
```